Plinqo, a service provider dedicated to improving the performance of a website

Plinqo offers optimization and performance improvement for all types of websites (showcase sites, e-commerce, ...), with the aim of improving their ranking on Searvo and their customer transformation rate. The main benefits consist in optimizing the factors of a site. In addition, we also offer content creation (description of product sheets, services, ...), Searvo Ads campaign management, migration version for Cartlume / Quillbase, etc. The design must be a fresh image, dynamic, why not "fun", but also serious. No favorite color, carte blanche on this point;)

```html
<!DOCTYPE html>
<html lang="en">
<head>
<meta charset="utf-8">
<title>Plinqo business card</title>
<link href="https://fonts.googleapis.com/css2?family=Work+Sans:wght@400;500;600;700&display=swap" rel="stylesheet">
<style>
  :root {
    --canvas: #e9eaee;
    --card-dark: #343436;
    --card-light: #ffffff;
    --brand-blue: #3853a3;
    --logo-dark: #1e1e20;
    --text-grey: #5e5e62;
    --text-light: #f2f2f2;
  }
  * { box-sizing: border-box; margin: 0; padding: 0; }
  html, body { width: 1200px; height: 881px; overflow: hidden; }
  body {
    background: var(--canvas);
    font-family: "Work Sans", Arial, sans-serif;
    display: flex;
    flex-direction: column;
    align-items: center;
    justify-content: center;
    gap: 34px;
  }
  .card {
    width: 680px;
    height: 390px;
    border-radius: 26px;
    border-bottom: 6px solid var(--brand-blue);
    box-shadow: 0 8px 22px rgba(0,0,0,0.18);
    position: relative;
    overflow: hidden;
  }
  /* back side */
  .card-back {
    background: var(--card-dark);
    display: flex;
    flex-direction: column;
    align-items: center;
    justify-content: center;
  }
  .card-back .brand-name {
    font-weight: 700;
    font-size: 140px;
    letter-spacing: -5px;
    line-height: 1;
    color: var(--logo-dark);
    white-space: nowrap;
  }
  .card-back .tagline {
    margin-top: 26px;
    color: var(--text-light);
    font-size: 17px;
    letter-spacing: 1.2px;
    line-height: 1.35;
    text-align: center;
  }
  /* front side */
  .card-front {
    background: var(--card-light);
    display: flex;
    align-items: center;
    padding: 0 44px 0 52px;
  }
  .card-front .brand-name {
    flex: none;
    font-weight: 700;
    font-size: 92px;
    letter-spacing: -3px;
    line-height: 1;
    color: var(--brand-blue);
    white-space: nowrap;
  }
  .divider {
    flex: none;
    width: 2px;
    height: 170px;
    background: var(--brand-blue);
    margin: 0 30px 0 28px;
  }
  .contact { flex: none; color: var(--text-grey); font-size: 16px; letter-spacing: 1.5px; line-height: 1.4; }
  .contact .person-name {
    color: var(--brand-blue);
    font-weight: 700;
    font-size: 21px;
    letter-spacing: 0.6px;
  }
  .contact .role { margin-bottom: 6px; }
  .contact .address { margin-bottom: 8px; }
  .contact-line { display: flex; align-items: center; gap: 10px; }
  .contact-line svg { width: 13px; height: 13px; flex: none; }
</style>
</head>
<body>
  <section class="card card-back">
    <div class="brand-name">Plinqo</div>
    <p class="tagline">Searvo Ads campaign management<br>migration version for Cartlume / Quillbase, etc.</p>
  </section>

  <section class="card card-front">
    <div class="brand-name">Plinqo</div>
    <div class="divider"></div>
    <div class="contact">
      <div class="person-name">DANIEL REYES</div>
      <div class="role">Director</div>
      <div class="address">214 Harbor Lane<br>Riverton, NJ 08077</div>
      <div class="contact-line">
        <svg viewBox="0 0 24 24" fill="#3853a3" aria-hidden="true"><path d="M6.6 10.8a15.1 15.1 0 0 0 6.6 6.6l2.2-2.2a1 1 0 0 1 1-.25 11.4 11.4 0 0 0 3.6.6 1 1 0 0 1 1 1V20a1 1 0 0 1-1 1A17 17 0 0 1 3 4a1 1 0 0 1 1-1h3.5a1 1 0 0 1 1 1c0 1.25.2 2.45.6 3.6a1 1 0 0 1-.25 1z"/></svg>
        <span>555 014-2290</span>
      </div>
      <div class="contact-line">
        <svg viewBox="0 0 24 24" fill="none" stroke="#3853a3" stroke-width="2.2" aria-hidden="true"><rect x="3" y="5" width="18" height="14" rx="1"/><path d="M3 6l9 7 9-7"/></svg>
        <span>info@plinqo.com</span>
      </div>
      <div class="contact-line">
        <svg viewBox="0 0 24 24" fill="none" stroke="#3853a3" stroke-width="2" aria-hidden="true"><circle cx="12" cy="12" r="9"/><path d="M3 12h18M12 3c3 3 3 15 0 18M12 3c-3 3-3 15 0 18"/></svg>
        <span>www.plinqo.com</span>
      </div>
    </div>
  </section>
</body>
</html>
```